Corvana Power Holdings Website

We have color scheme, logo and content, but need a design options in PDF format for the website. The PDF should guide us in how to use the color scheme and fonts in the site design (what background colors to use where, what link and hover colors to you, when to use which fonts...)

Corvana Power Holdings wants a conservative and straightforward website design that is in line with the banking industry. At the same time, Corvana wants the design to be innovative and cutting-edge in line with the renewable energy industry. Overall, the site design must be present the company as professional, serious, knowledgeable, experienced, reliable, and successful as well as a global good citizen.
Updates

We are closing this project. Thank you all for your beautiful work. Our designer was sick, but informed us today that she is better and able to resume her work. So we are closing this project and restarting work with her. Wish you all health and success.

Target Market(s)

investors, partners, developers, investment community, private equity community

Industry/Entity Type

Investment

Number of Pages Required

2 page

Requirements
Must have
• The color scheme is attached.
The logo is attached.
Fonts are Questrial and Cormorant (as used in logo).
The site must use these colors and fonts and logo design.

The 2 pages we need designed are the homepage and the portfolio page.
Homepage - The portfolio map on the homepage will be an image like with hotspots that link to portfolio items. This map image might go well with logo:
https://www.pixdrovo.com/abstract-polygon-world-map-vector-illustration-geometric-structure-in-blue-color-for-presentation-booklet-website-and-other-design-projects-pol-image550392817.html
But we would need to zoom in on Israel and EU, and leave out US / Asia-Pacific.
The way the map will work technically (using hotspots) should be something like:
https://tarvimpower.co.il/geographic-spread/.
Portfolio Page - The portfolio map there will be a Google Map/
Nice to have
• The content for the site is attached as a Word Doc, and much of it is in place at http://corvanafund.com.node4821.hostmarvo.de/. The design must fit this content, but we are open to some layout changes.
Design Requests:
• nav bar – light animation like https://pelludovet.com/ and https://www.qz-relocationlaw.com/
• innovative, unique design with welcoming, appealing, modern feel
• engaging content display by using parallax and subtle movement
• clean, intuitive, easy to navigation layout

```html
<!DOCTYPE html>
<html lang="en">
<head>
<meta charset="utf-8">
<title>Corvana Power Holdings</title>
<link href="https://fonts.googleapis.com/css2?family=Cormorant+Garamond:wght@600;700&family=Questrial&family=Poppins:wght@400;700&display=swap" rel="stylesheet">
<style>
:root{
  --green:#5ba25c;
  --green-deep:#1d5c3b;
  --lime:#b3d335;
  --blue:#3a86c6;
  --blue-link:#2d7fc4;
  --orange:#f7ae4f;
  --yellow:#f6e73a;
  --sky:#4fa8e3;
  --footer:#123231;
  --text:#333;
  --muted:#666;
  --white:#fff;
}
*{margin:0;padding:0;box-sizing:border-box}
html,body{width:1200px;height:3188px;overflow:hidden}
body{font-family:'Questrial',sans-serif;color:var(--text);background:var(--white);position:relative}
.abs{position:absolute}
.btn{position:absolute;display:flex;align-items:center;justify-content:center;color:var(--white);font-size:20px;border-radius:3px;background:linear-gradient(90deg,var(--lime),var(--blue));letter-spacing:.3px}
/* header */
.site-header{position:absolute;left:0;top:0;width:1200px;height:83px;border-top:3px solid var(--lime);background:var(--white)}
.brand{position:absolute;left:78px;top:22px;display:flex;align-items:center;gap:10px}
.brand-dot{width:40px;height:40px;border-radius:50%;background:var(--lime)}
.brand-name{font-family:'Cormorant Garamond',serif;font-weight:700;font-size:26px;color:var(--green-deep);letter-spacing:.5px}
.nav{position:absolute;top:33px;left:758px;display:flex;gap:23px;font-size:14px;color:#222;letter-spacing:.3px}
.nav .active{color:var(--green);display:flex;align-items:center;gap:10px}
.nav .active:before{content:"";width:10px;height:10px;border-radius:50%;background:var(--lime);border:2px solid var(--green)}
/* hero */
.hero{position:absolute;left:0;top:83px;width:1200px;height:594px;background:linear-gradient(180deg,#4b5660 0%,#5d6a6c 35%,#3e5848 60%,#2b3f3a 100%)}
.hero-title{position:absolute;left:0;width:1200px;top:170px;text-align:center;font-family:'Cormorant Garamond',serif;font-weight:700;font-size:54px;line-height:57px;color:var(--white);letter-spacing:1px}
.hero-sub{position:absolute;left:300px;width:600px;top:292px;text-align:center;font-size:19px;line-height:29px;color:var(--white)}
.hero-arrow{position:absolute;top:271px;width:52px;height:52px;border-radius:50%;border:1.5px solid var(--white)}
.hero-arrow.right{border-color:var(--lime)}
/* cards */
.card{position:absolute;background:var(--white);border-radius:10px;box-shadow:0 4px 20px rgba(0,0,0,.08)}
.card-photo{position:absolute;border-radius:6px}
.card-title{position:absolute;width:100%;text-align:center;font-size:18px;line-height:25px;color:var(--green-deep);letter-spacing:.3px}
.card-text{position:absolute;text-align:center;font-size:15px;line-height:27px;color:var(--muted)}
/* stats */
.stats{position:absolute;left:0;top:1496px;width:1200px;height:354px;background:linear-gradient(180deg,#5e9e68,#5aa35a 60%,#4f9a55)}
.stat{position:absolute;top:72px;width:209px;height:208px;background:var(--white);text-align:center}
.stat svg{position:absolute;left:76px;top:26px}
.stat-num{position:absolute;top:96px;width:100%;font-family:'Poppins',sans-serif;font-weight:700;font-size:26px;color:var(--green-deep)}
.stat-label{position:absolute;top:146px;width:100%;font-size:18px;line-height:23px;color:#333}
/* quote */
.dot{position:absolute;border-radius:50%}
.quote-mark{position:absolute;left:636px;top:1995px;width:79px;height:79px;border-radius:50%;background:linear-gradient(135deg,var(--lime),var(--blue))}
.quote-text{position:absolute;left:631px;top:2090px;width:440px;font-size:19.5px;line-height:33.5px;color:#333}
.quote-link{position:absolute;left:671px;top:2306px;width:420px;font-size:15.5px;line-height:25px;color:var(--blue-link)}
.quote-rule{position:absolute;left:632px;top:2317px;width:24px;height:2px;background:var(--blue-link)}
/* cta */
.cta{position:absolute;left:0;top:2567px;width:1200px;height:325px;background:linear-gradient(180deg,#3d7fb8,#3e86bf 50%,#3a7cae)}
.cta-text{position:absolute;left:200px;width:800px;top:90px;text-align:center;font-size:29px;line-height:40px;color:var(--white)}
/* footer */
.site-footer{position:absolute;left:0;top:2892px;width:1200px;height:296px;background:var(--footer);color:var(--white)}
.footer-heading{position:absolute;top:46px;font-family:'Cormorant Garamond',serif;font-weight:600;font-size:23px;color:var(--lime);letter-spacing:1px}
.contact-row{position:absolute;left:78px;display:flex;align-items:center;gap:14px;font-size:15.5px}
.footer-brand{position:absolute;left:445px;top:97px;display:flex;align-items:center;gap:14px}
.footer-brand .brand-dot{width:58px;height:58px}
.footer-brand .brand-name{color:var(--white);font-size:40px}
.address{position:absolute;right:118px;top:94px;text-align:right;font-size:15.5px;line-height:27px}
.footer-rule{position:absolute;left:78px;top:220px;width:1044px;height:1px;background:rgba(255,255,255,.15)}
.copyright{position:absolute;top:250px;width:1200px;text-align:center;font-size:14.5px}
.copyright span{color:var(--lime)}
</style>
</head>
<body>

<header class="site-header">
  <div class="brand"><span class="brand-dot"></span><span class="brand-name">Corvana Power Holdings</span></div>
  <nav class="nav"><span class="active">HOME</span><span>STARTEGY</span><span>PORTFOLIO</span><span>CONTACT</span></nav>
</header>

<section class="hero" role="img" aria-label="Aerial photo of a lake and industrial landscape under a cloudy sky">
  <span class="hero-arrow" style="left:12px"></span>
  <span class="hero-arrow right" style="left:1134px"></span>
  <h1 class="hero-title">ILLUMINATING THE<br>FUTURE</h1>
  <p class="hero-sub">Investing in clean energy to generate sustainable returns for our investors and planet</p>
  <a class="btn" style="left:501px;top:365px;width:198px;height:57px">CONTACT US</a>
</section>

<section class="services">
  <article class="card" style="left:226px;top:748px;width:354px;height:481px">
    <div class="card-photo" role="img" aria-label="Photo of hands typing on a laptop showing financial charts" style="left:22px;top:19px;width:312px;height:213px;background:linear-gradient(135deg,#dfe6ec,#8e9ba6 55%,#3c4650)"></div>
    <h2 class="card-title" style="top:257px">HANDS-ON INVESTMENT<br>MANAGEMENT</h2>
    <p class="card-text" style="left:40px;width:274px;top:325px">Funding clean energy projects that maximise value to our investors and contribute to a more sustainable world</p>
  </article>
  <a class="btn" style="left:320px;top:1205px;width:166px;height:57px">ABOUT US</a>

  <article class="card" style="left:620px;top:907px;width:353px;height:478px">
    <div class="card-photo" role="img" aria-label="Photo of colleagues meeting around a laptop in an office" style="left:21px;top:15px;width:312px;height:213px;background:linear-gradient(135deg,#e7ebee,#9aa3ab 50%,#3a3f48)"></div>
    <h2 class="card-title" style="top:249px">EXPERTISE. RESOUR -<br>CEFULNESS. INTEGRITY</h2>
    <p class="card-text" style="left:40px;width:273px;top:320px">Utilising our multi-disciplinary knowledge, sector expertise, extensive experience and colla - borative spirit.</p>
  </article>
  <a class="btn" style="left:707px;top:1359px;width:172px;height:57px">OUR TEAM</a>
</section>

<section class="stats" role="img" aria-label="Green-tinted photo of solar panels on rolling fields">
  <div class="stat" style="left:153px">
    <svg width="58" height="58" viewBox="0 0 58 58"><circle cx="29" cy="29" r="25" fill="none" stroke="#1d5c3b" stroke-width="4" stroke-dasharray="30 8"/><circle cx="29" cy="29" r="16" fill="#1d5c3b"/><circle cx="29" cy="29" r="6" fill="#fff"/></svg>
    <div class="stat-num">10</div><div class="stat-label">Years of<br>Operation</div>
  </div>
  <div class="stat" style="left:382px">
    <svg width="58" height="58" viewBox="0 0 58 58"><circle cx="29" cy="27" r="24" fill="none" stroke="#1d5c3b" stroke-width="4"/><circle cx="29" cy="27" r="16" fill="#1d5c3b"/><text x="29" y="35" text-anchor="middle" font-family="Poppins,sans-serif" font-weight="700" font-size="22" fill="#fff">$</text></svg>
    <div class="stat-num">06</div><div class="stat-label">Countries of<br>Investments</div>
  </div>
  <div class="stat" style="left:610px">
    <svg width="58" height="58" viewBox="0 0 58 58"><circle cx="22" cy="10" r="7" fill="#1d5c3b"/><rect x="14" y="19" width="16" height="36" rx="3" fill="#1d5c3b"/><rect x="32" y="34" width="18" height="18" fill="#1d5c3b"/></svg>
    <div class="stat-num">100</div><div class="stat-label">MW under<br>Management</div>
  </div>
  <div class="stat" style="left:838px">
    <svg width="58" height="58" viewBox="0 0 58 58"><circle cx="29" cy="29" r="25" fill="none" stroke="#1d5c3b" stroke-width="5" stroke-dasharray="9 4"/><circle cx="29" cy="29" r="17" fill="#1d5c3b"/><circle cx="29" cy="24" r="5" fill="#fff"/><path d="M20 40 q9 -12 18 0z" fill="#fff"/></svg>
    <div class="stat-num">€500,000,000</div><div class="stat-label">Assets under<br>Management</div>
  </div>
</section>

<section class="portfolio-quote">
  <span class="dot" style="left:134px;top:1927px;width:52px;height:52px;background:var(--orange)"></span>
  <span class="dot" role="img" aria-label="Photo of electrical switchgear cabinets" style="left:252px;top:1917px;width:204px;height:204px;background:linear-gradient(135deg,#e1d9c8,#b29a78 50%,#6e6e68)"></span>
  <span class="dot" role="img" aria-label="Photo of a wind turbine over farmland" style="left:-80px;top:2083px;width:335px;height:331px;background:linear-gradient(180deg,#c5d0dc,#8c9a8e 55%,#5d6d48)"></span>
  <span class="dot" style="left:302px;top:2167px;width:31px;height:31px;background:var(--sky)"></span>
  <span class="dot" style="left:391px;top:2184px;width:46px;height:46px;background:var(--lime)"></span>
  <span class="dot" role="img" aria-label="Photo of a rural energy facility under cloudy skies" style="left:306px;top:2258px;width:195px;height:195px;background:linear-gradient(180deg,#9fbbd6,#d5dde3 45%,#5f7d56)"></span>
  <span class="dot" style="left:204px;top:2427px;width:36px;height:36px;background:var(--yellow)"></span>
  <span class="dot" style="left:-22px;top:2452px;width:72px;height:72px;background:var(--green)"></span>

  <div class="quote-mark"><svg width="79" height="79" viewBox="0 0 79 79"><text x="39.5" y="66" text-anchor="middle" font-family="Cormorant Garamond,serif" font-weight="700" font-size="70" fill="#fff">“</text></svg></div>
  <p class="quote-text">" Corvana’ energy funds provide a diversified portfolio of assets - in operation and under construction, in multiple markets - that drive high investment returns and a balanced risk profile. "</p>
  <span class="quote-rule"></span>
  <p class="quote-link">Map (focused on UK, Italy, Spain, Israel, Poland and the Netherlands)<br>with links to individual portfolio items</p>
</section>

<section class="cta" role="img" aria-label="Blue-tinted aerial photo of an industrial site">
  <p class="cta-text">For More Information, Please Fill in this Form. We will Respond as Soon as Possible.</p>
  <a class="btn" style="left:507px;top:191px;width:187px;height:57px;background:var(--green)">CONTACT US</a>
</section>

<footer class="site-footer">
  <h3 class="footer-heading" style="left:79px">CONTACT INFO</h3>
  <div class="contact-row" style="top:98px"><svg width="20" height="20" viewBox="0 0 24 24"><path d="M6.6 10.8a15 15 0 0 0 6.6 6.6l2.2-2.2a1 1 0 0 1 1-.25 11.4 11.4 0 0 0 3.6.57 1 1 0 0 1 1 1V20a1 1 0 0 1-1 1A17 17 0 0 1 3 4a1 1 0 0 1 1-1h3.5a1 1 0 0 1 1 1c0 1.25.2 2.45.57 3.6a1 1 0 0 1-.25 1z" fill="#b3d335"/></svg>Israel:&nbsp; +972-3-555-0148</div>
  <div class="contact-row" style="top:136px"><svg width="20" height="20" viewBox="0 0 24 24"><path d="M6.6 10.8a15 15 0 0 0 6.6 6.6l2.2-2.2a1 1 0 0 1 1-.25 11.4 11.4 0 0 0 3.6.57 1 1 0 0 1 1 1V20a1 1 0 0 1-1 1A17 17 0 0 1 3 4a1 1 0 0 1 1-1h3.5a1 1 0 0 1 1 1c0 1.25.2 2.45.57 3.6a1 1 0 0 1-.25 1z" fill="#b3d335"/></svg>Europe: +44 (0) 20 7946 0321</div>
  <div class="contact-row" style="top:176px"><svg width="20" height="16" viewBox="0 0 20 16"><rect width="20" height="16" rx="2" fill="#b3d335"/><path d="M1 2l9 7 9-7" fill="none" stroke="#123231" stroke-width="1.8"/></svg>info@corvanafund.com</div>

  <div class="footer-brand"><span class="brand-dot"></span><span class="brand-name">Corvana</span></div>

  <h3 class="footer-heading" style="right:78px">KEEP IN TOUCH</h3>
  <p class="address">Meridan Building, Givat Oren<br>Ramat Halev, Ramat Halev<br>47950 Israel</p>
  <svg class="abs" style="left:1100px;top:98px" width="22" height="30" viewBox="0 0 22 30"><path d="M11 2a8.5 8.5 0 0 0-8.5 8.5C2.5 17 11 27 11 27s8.5-10 8.5-16.5A8.5 8.5 0 0 0 11 2z" fill="none" stroke="#b3d335" stroke-width="2.2"/><circle cx="11" cy="10.5" r="3" fill="#b3d335"/></svg>

  <div class="footer-rule"></div>
  <p class="copyright">© 2020 <span>Corvana Power Holdings</span> -All rights eserved.</p>
</footer>

</body>
</html>
```